Solar energy proposal for homeowners

I am providing households with solar energy proposals, and I need a high-quality brochure that is packaged cleverly to attract the homeowner's attention. Take a look at the one page solar brochure that I have included to get an idea of text and content.

Target Market(s)

Residential Homeowners

Industry/Entity Type

Solar

Requirements
Must have
• High quality document

```html
<!DOCTYPE html>
<html lang="en">
<head>
<meta charset="utf-8">
<title>Brightvale Energy – Solar for $0 Down</title>
<link href="https://fonts.googleapis.com/css2?family=Montserrat:wght@400;500;600;700;800&display=swap" rel="stylesheet">
<style>
  :root{
    --navy:#0b1d48;
    --navy-deep:#081638;
    --teal:#0f7fa6;
    --teal-bright:#14b3cf;
    --lime:#b6e01e;
    --ink:#132a5c;
    --text:#1d2434;
    --white:#ffffff;
    --photo-a:#2f5f9e;
    --photo-b:#27508a;
  }
  *{margin:0;padding:0;box-sizing:border-box}
  html,body{width:731px;height:1200px;overflow:hidden;background:#fff}
  body{font-family:"Montserrat",sans-serif;color:var(--text)}
  .flyer{position:relative;width:731px;height:1200px;overflow:hidden;background:var(--white)}
  .backdrop{position:absolute;inset:0}
  .brand{position:absolute;left:44px;top:50px;display:flex;align-items:center;gap:12px}
  .brand-mark{width:26px;height:26px;background:var(--teal-bright)}
  .brand-name{font-size:26px;font-weight:400;color:var(--teal-bright);letter-spacing:.3px;line-height:1}
  .headline{position:absolute;left:40px;top:172px;font-weight:800;font-size:37px;line-height:41px;text-transform:uppercase;color:var(--white)}
  .headline .accent{color:var(--lime)}
  .tagline{position:absolute;left:42px;top:383px;font-size:10px;font-weight:500;color:var(--white);text-transform:uppercase}
  .section-title{font-weight:700;font-size:22px;color:var(--ink);text-transform:uppercase}
  .about{position:absolute;left:44px;top:490px;width:330px}
  .about p{margin-top:16px;font-size:14.2px;line-height:24px;text-align:justify}
  .why{position:absolute;left:408px;top:556px;width:300px}
  .why ul{list-style:none;margin-top:16px}
  .why li{display:flex;align-items:center;gap:10px;font-size:14.5px;line-height:24px;font-weight:500}
  .why li b{color:var(--ink);font-weight:700}
  .tick{width:12px;height:12px;flex:none}
  .services-title{position:absolute;left:0;right:0;top:800px;display:flex;align-items:center;gap:18px;color:var(--white);font-weight:700;font-size:22px;text-transform:uppercase}
  .services-title::before,.services-title::after{content:"";height:2px;background:var(--lime);flex:1}
  .service{position:absolute;width:285px;display:flex;gap:10px;color:var(--white)}
  .service-icon{width:26px;height:26px;flex:none;margin-top:2px}
  .service h3{font-size:14.5px;font-weight:700;color:var(--lime);text-transform:uppercase;line-height:18px}
  .service p{font-size:14.5px;line-height:19px;margin-top:5px}
  .contact-title{position:absolute;left:0;right:0;top:1090px;text-align:center;color:var(--white);font-weight:700;font-size:22px;text-transform:uppercase}
  .contact-row{position:absolute;left:0;right:0;top:1160px;display:flex;justify-content:center;gap:18px;font-size:12.5px;font-weight:700;color:var(--ink);text-transform:uppercase}
  .contact-row span{display:flex;align-items:center;gap:7px}
  .contact-row svg{width:13px;height:13px}
</style>
</head>
<body>
<main class="flyer">
  <svg class="backdrop" width="731" height="1200" viewBox="0 0 731 1200">
    <defs>
      <linearGradient id="header-fill" x1="0" y1="0" x2="1" y2="1">
        <stop offset="0" stop-color="#0c2a5a"/>
        <stop offset="1" stop-color="#071434"/>
      </linearGradient>
      <linearGradient id="band-fill" x1="0" y1="0" x2="0" y2="1">
        <stop offset="0" stop-color="#0a2e63"/>
        <stop offset=".55" stop-color="#0d74a0"/>
        <stop offset="1" stop-color="#15b0cc"/>
      </linearGradient>
      <linearGradient id="logo-band" x1="0" y1="0" x2="1" y2="0">
        <stop offset="0" stop-color="#0e5d80"/>
        <stop offset="1" stop-color="#0a3c68"/>
      </linearGradient>
      <linearGradient id="photo-fill" x1="0" y1="0" x2="0" y2="1">
        <stop offset="0" stop-color="var(--photo-a)"/>
        <stop offset="1" stop-color="var(--photo-b)"/>
      </linearGradient>
      <linearGradient id="tab-fill" x1="0" y1="0" x2="0" y2="1">
        <stop offset="0" stop-color="#14b8d2"/>
        <stop offset="1" stop-color="#0e8fb4"/>
      </linearGradient>
    </defs>
    <polygon points="0,0 731,0 731,535 440,535 390,430 0,430" fill="url(#header-fill)"/>
    <polygon points="0,0 430,0 350,143 0,143" fill="url(#logo-band)"/>
    <rect x="0" y="783" width="731" height="307" fill="url(#band-fill)"/>
    <path d="M110,1090 Q150,1090 175,1112 Q195,1128 230,1128 L500,1128 Q535,1128 555,1112 Q580,1090 620,1090 Z" fill="url(#tab-fill)"/>
    <g role="img" aria-label="Photo of solar panels on green grass under a blue sky">
      <polygon points="302,271 419,13 676,13 790,271 676,519 419,519" fill="url(#photo-fill)" stroke="var(--lime)" stroke-width="4"/>
    </g>
  </svg>

  <div class="brand">
    <span class="brand-mark"></span>
    <span class="brand-name">brightvale energy</span>
  </div>

  <h1 class="headline">
    <span class="accent">Solar for<br>$0 Down.</span><br>No Liens.<br>No Kidding.
  </h1>
  <p class="tagline">Power your future with Brightvale Energy</p>

  <section class="about">
    <h2 class="section-title">About Us</h2>
    <p>At Brightvale Energy. our mission is to make solar simple and accessible for everyone. No high-pressure sales-just the information you need to make a smart choice. with our solar rental program. you can lower your monthly energy costs and pay less than your current electricity bill.</p>
  </section>

  <section class="why">
    <h2 class="section-title">Why Choose Us?</h2>
    <ul>
      <li><svg class="tick" viewBox="0 0 12 12"><circle cx="6" cy="6" r="6" fill="var(--text)"/><path d="M3.2 6.2l2 2 3.6-4" stroke="#fff" stroke-width="1.6" fill="none"/></svg><span><b>No</b> financing</span></li>
      <li><svg class="tick" viewBox="0 0 12 12"><circle cx="6" cy="6" r="6" fill="var(--text)"/><path d="M3.2 6.2l2 2 3.6-4" stroke="#fff" stroke-width="1.6" fill="none"/></svg><span><b>No</b> liens</span></li>
      <li><svg class="tick" viewBox="0 0 12 12"><circle cx="6" cy="6" r="6" fill="var(--text)"/><path d="M3.2 6.2l2 2 3.6-4" stroke="#fff" stroke-width="1.6" fill="none"/></svg><span><b>No</b> down payment</span></li>
      <li><svg class="tick" viewBox="0 0 12 12"><circle cx="6" cy="6" r="6" fill="var(--text)"/><path d="M3.2 6.2l2 2 3.6-4" stroke="#fff" stroke-width="1.6" fill="none"/></svg><span><b>No</b> insurance costs</span></li>
      <li><svg class="tick" viewBox="0 0 12 12"><circle cx="6" cy="6" r="6" fill="var(--text)"/><path d="M3.2 6.2l2 2 3.6-4" stroke="#fff" stroke-width="1.6" fill="none"/></svg><span><b>No</b> long-term commitment</span></li>
      <li><svg class="tick" viewBox="0 0 12 12"><circle cx="6" cy="6" r="6" fill="var(--text)"/><path d="M3.2 6.2l2 2 3.6-4" stroke="#fff" stroke-width="1.6" fill="none"/></svg><span><b>No</b> maintenance costs</span></li>
    </ul>
  </section>

  <h2 class="services-title">Our Best Service</h2>

  <div class="service" style="left:34px;top:850px">
    <svg class="service-icon" viewBox="0 0 26 26"><circle cx="13" cy="13" r="13" fill="var(--lime)"/><rect x="8" y="7" width="10" height="12" rx="1" fill="none" stroke="var(--navy)" stroke-width="1.6"/><path d="M10.5 11h5M10.5 14h5" stroke="var(--navy)" stroke-width="1.4"/></svg>
    <div><h3>Affordable &amp; Transparent</h3><p>simple pricing, no hidden fees and a fixed monthly rate lower than typical energy bills.</p></div>
  </div>
  <div class="service" style="left:383px;top:850px">
    <svg class="service-icon" viewBox="0 0 26 26"><circle cx="13" cy="13" r="13" fill="var(--lime)"/><circle cx="13" cy="13" r="5" fill="none" stroke="var(--navy)" stroke-width="2.2" stroke-dasharray="2.5 1.5"/><circle cx="13" cy="13" r="1.8" fill="var(--navy)"/></svg>
    <div><h3>Expert Installation</h3><p>Certified professionals handle installation, maintenance, and repairs end to end.</p></div>
  </div>
  <div class="service" style="left:34px;top:970px">
    <svg class="service-icon" viewBox="0 0 26 26"><circle cx="13" cy="13" r="13" fill="var(--lime)"/><circle cx="13" cy="11" r="5" fill="none" stroke="var(--navy)" stroke-width="1.8"/><path d="M10 15l-1.5 5 4.5-2 4.5 2-1.5-5" fill="none" stroke="var(--navy)" stroke-width="1.6"/></svg>
    <div><h3>Local Expertise</h3><p>Florida-based team that under-stands the needs of Orlando and Statewide homeowners.</p></div>
  </div>
  <div class="service" style="left:383px;top:970px">
    <svg class="service-icon" viewBox="0 0 26 26"><circle cx="13" cy="13" r="13" fill="var(--lime)"/><path d="M13 19c0-5 2-8 6-9-1 5-3 8-6 9zM13 19c0-4-2-6-5-7 0 4 2 6 5 7z" fill="var(--navy)"/></svg>
    <div><h3>Eco-Friendly</h3><p>Clean, renewable solar energy that helps reduce your carbon footprint.</p></div>
  </div>

  <h2 class="contact-title">Contact Us</h2>
  <div class="contact-row">
    <span><svg viewBox="0 0 14 14"><path d="M3 1l2.5 3-1.3 1.5a8 8 0 0 0 4.3 4.3L10 8.5l3 2.5-1.5 2C6 13 1 8 1 2.5z" fill="none" stroke="var(--ink)" stroke-width="1.5"/></svg>(555)010-2478</span>
    <span><svg viewBox="0 0 14 14"><rect x="1" y="3" width="12" height="8" fill="var(--ink)"/><path d="M1 3l6 5 6-5" stroke="#fff" stroke-width="1" fill="none"/></svg>123 Anywhere St. Any City</span>
    <span><svg viewBox="0 0 14 14"><circle cx="7" cy="7" r="6" fill="none" stroke="var(--ink)" stroke-width="1.3"/><ellipse cx="7" cy="7" rx="2.6" ry="6" fill="none" stroke="var(--ink)" stroke-width="1.1"/><path d="M1 7h12" stroke="var(--ink)" stroke-width="1.1"/></svg>www.brightvaleenergy.com</span>
  </div>
</main>
</body>
</html>
```